Wellness/ Medical Fitness Company Seeks Promotional Brochure

We need a 4 page brochure for the launch of our new business next month. We are combining science and medicine with the fitness and wellness industry. We are unique in that we are using cutting edge technology and monitoring devices to create customized workouts and training. We offer group classes and individual training.We are looking for a professional promotion brochure that has sleek and modern look and feel to it. We would like to use the colors of our logo in the design. We are a company made up of young people so we would like to have a future and modern vibe to the design.

Target Market(s)

18-65 male and female

Industry/Entity Type

Medical

Colors

Designer to choose colors to be used in the design.

Requirements
Must have
• Modern, sleek look
• Marketing to a professional demographic
Should not have
• No gaudy or tacky colors

```html
<!DOCTYPE html>
<html lang="en">
<head>
<meta charset="utf-8">
<title>Vela Wellness Brochure</title>
<link href="https://fonts.googleapis.com/css2?family=Mulish:ital,wght@0,300;0,400;0,600;0,700;0,800;1,400&family=Oswald:wght@500;700&display=swap" rel="stylesheet">
<style>
:root{
  --stage:#dcdcdc;
  --paper:#ffffff;
  --paper-soft:#f1f1f1;
  --sand:#c8aa86;
  --sand-light:#e4d3bd;
  --sand-pale:#f0e6d8;
  --ink:#2f2f2f;
  --ink-soft:#5e5e5e;
  --grey:#8a8a8a;
  --grey-light:#bdbdbd;
  --pill:#5a5a5a;
}
*{box-sizing:border-box;margin:0;padding:0}
html,body{width:1098px;height:1200px;overflow:hidden}
body{background:var(--stage);font-family:'Mulish',Arial,sans-serif;color:var(--ink-soft);position:relative}
.spread{position:absolute;left:39px;width:1020px;height:540px;display:flex;box-shadow:0 6px 18px rgba(0,0,0,.18)}
.spread--outer{top:40px}
.spread--inner{top:620px}
.page{position:relative;width:510px;height:540px;background:var(--paper);overflow:hidden}
.page + .page{border-left:1px solid #e6e6e6}
.page--cover{background:linear-gradient(160deg,#f7f7f7,#ebebeb)}

/* brand lockup */
.brand{display:flex;align-items:center;gap:8px;color:var(--grey)}
.brand__dot{width:22px;height:22px;border-radius:50%;background:var(--grey-light)}
.brand__name{font-weight:400;letter-spacing:3px;font-size:20px;line-height:1;white-space:nowrap}

/* back cover */
.about{position:absolute;left:60px;top:60px;width:330px;height:330px;background:linear-gradient(135deg,var(--sand-light),var(--sand));padding:70px 30px 0 26px;color:var(--ink-soft)}
.about__title{font-size:17px;font-weight:400;display:flex;align-items:center;gap:8px;color:#4a4a4a}
.about__title::after{content:"";flex:1;height:1px;background:#6f6255}
.about__text{font-size:11px;line-height:1.45;margin-top:6px;color:#4f4a44}
.about__claim{font-size:27px;font-weight:300;line-height:1.3;margin-top:48px;color:#4a4540}
.about__claim strong{font-weight:800;color:#fff}
.back-foot{position:absolute;left:60px;right:40px;top:420px;border-top:1px solid #ddd;padding-top:26px;display:flex;gap:18px}
.back-foot .brand{flex-direction:column;align-items:flex-start;gap:4px}
.links{border-left:1px solid #ccc;padding-left:14px;list-style:none;font-size:11px;color:var(--ink-soft);line-height:1.9}
.links li{display:flex;align-items:center;gap:8px}
.links li::before{content:"";width:8px;height:8px;border-radius:50%;background:var(--grey)}

/* front cover */
.cover-brand{position:absolute;left:30px;top:34px;flex-direction:column;align-items:flex-start;gap:6px}
.cover-brand .brand__name{font-size:22px;letter-spacing:3px}
.photo{position:absolute;border-radius:50%;border:6px solid #fff;box-shadow:0 2px 8px rgba(0,0,0,.2)}
.photo--main{left:50px;top:100px;width:245px;height:245px;background:radial-gradient(circle at 45% 40%,#5d6166,#25282c 70%)}
.photo--top{left:255px;top:40px;width:128px;height:128px;background:radial-gradient(circle at 50% 45%,#b7b1ab,#6d6864)}
.photo--side{left:280px;top:235px;width:100px;height:100px;background:radial-gradient(circle at 50% 45%,#d8c19a,#7a6a55)}
.ring{position:absolute;right:-60px;top:300px;width:200px;height:200px;border-radius:50%;border:22px solid rgba(0,0,0,.05)}
.headline{position:absolute;left:30px;top:370px;font-family:'Oswald',Impact,sans-serif;font-weight:700;font-size:37px;line-height:1.08;color:var(--ink);letter-spacing:.3px}
.headline span{display:block;color:var(--grey)}
.cover-url{position:absolute;left:30px;right:30px;top:472px;display:flex;align-items:center;gap:10px;font-size:15px;font-weight:600;color:var(--ink-soft)}
.cover-url::before{content:"";flex:1;height:1px;background:#bbb}

/* inner left */
.intro{position:absolute;left:34px;top:60px;width:430px;font-size:10.5px;line-height:1.45}
.intro p + p{margin-top:8px}
.statement{position:absolute;left:34px;top:138px;font-size:24px;font-weight:400;color:var(--ink);line-height:1.15;letter-spacing:.4px}
.statement span{font-size:27px}
.pill{position:absolute;left:0;top:218px;background:var(--pill);color:#fff;font-size:14px;letter-spacing:1px;padding:5px 26px 5px 34px;border-radius:0 16px 16px 0}
.programs{position:absolute;left:34px;top:248px;display:flex;gap:40px}
.programs ul{list-style:none;font-size:12px;color:var(--ink-soft);line-height:1.7}
.programs li{display:flex;gap:7px;align-items:flex-start}
.programs svg{flex:none;margin-top:3px}
.note{position:absolute;left:250px;top:332px;font-size:9px;font-style:italic;color:var(--ink-soft)}

/* pricing band across inner spread */
.pricing{position:absolute;left:0;top:346px;width:1020px;height:194px;background:linear-gradient(180deg,var(--sand-pale),var(--sand));z-index:1}
.pricing__label{position:absolute;left:0;top:0;width:150px;background:#e0e0e0;font-size:15px;letter-spacing:1px;color:var(--ink);padding:4px 0 4px 34px}
.price-col{position:absolute;display:flex;flex-direction:column;gap:6px}
.price-col--fitness{left:34px;top:30px;width:170px}
.price-col--testing{left:212px;top:8px;width:196px}
.price-col--recovery{left:416px;top:8px;width:198px}
.price-box{background:#fff;padding:0 8px 5px;font-size:8px;color:var(--ink-soft);line-height:1.35}
.price-box h3{font-size:8px;font-weight:800;letter-spacing:.5px;text-align:center;color:var(--ink);background:var(--paper-soft);margin:0 -8px 4px;padding:3px 0;text-transform:uppercase}
.price-box .rate{text-align:center;font-weight:700;font-size:7px;margin-bottom:2px}
.price-box ul{padding-left:11px}
.price-box .fine{font-style:italic;font-size:7px;line-height:1.3}

/* inner right */
.device-title{position:absolute;left:24px;top:42px;font-size:15px;font-weight:800;color:var(--ink);display:flex;align-items:center;gap:10px;width:460px}
.device-title::after{content:"";flex:1;height:1px;background:#ccc}
.device-text{position:absolute;left:24px;top:66px;width:460px;font-size:10px;line-height:1.45}
.inner-brand{position:absolute;left:30px;top:175px;flex-direction:column;align-items:flex-start;gap:4px}
.inner-brand .brand__name{font-size:18px}
.shot{position:absolute;border-radius:50%;border:6px solid #fff;box-shadow:0 3px 10px rgba(0,0,0,.3);z-index:2}
.shot--main{left:205px;top:150px;width:280px;height:280px;background:radial-gradient(circle at 50% 35%,#3c2a3e,#0d0d10 70%)}
.shot--app{left:135px;top:320px;width:145px;height:145px;background:radial-gradient(circle at 50% 50%,#2b2b2e,#0b0b0c)}
.shot--band{left:260px;top:380px;width:155px;height:155px;background:radial-gradient(circle at 50% 50%,#3a3a3c,#0f0f10)}
</style>
</head>
<body>

<section class="spread spread--outer">
  <div class="page page--back">
    <div class="about">
      <h2 class="about__title">About Us</h2>
      <p class="about__text">Vela Wellness creates personalized data-driven solutions for your wellness goals. We believe in using customized assessments to create wellness ecosystems that fit your daily life.</p>
      <p class="about__claim">We are <strong>NOT JUST</strong> any gym or wellness center.</p>
    </div>
    <div class="back-foot">
      <div class="brand"><span class="brand__dot"></span><span class="brand__name">vela wellness</span></div>
      <ul class="links">
        <li>www.thevelawellness.com</li>
        <li>www.pictogram.net/velawellness</li>
        <li>www.friendsbook.net/velawellness</li>
      </ul>
    </div>
  </div>
  <div class="page page--cover">
    <div class="brand cover-brand"><span class="brand__dot"></span><span class="brand__name">vela wellness</span></div>
    <div class="ring"></div>
    <div class="photo photo--top" role="img" aria-label="Photo of two women training together in a gym"></div>
    <div class="photo photo--main" role="img" aria-label="Photo of a man training with battle ropes"></div>
    <div class="photo photo--side" role="img" aria-label="Photo of a woman working out"></div>
    <h1 class="headline">CREATED BY DOCTORS.<span>SUPPORTED BY SCIENCE.</span></h1>
    <p class="cover-url">www.thevelawellness.com</p>
  </div>
</section>

<section class="spread spread--inner">
  <div class="page inner-left">
    <div class="intro">
      <p>We are a science lab that is focused on using your biometric outputs to help you train, rest and recover better.</p>
      <p>Whether you want to hit the ball harder or you want to run faster or you just want to join our group classes to live healthier, we will help you achieve those goals.</p>
    </div>
    <h2 class="statement">EVERYTHING WE OFFER IS BACKED BY<br><span>SCIENCE AND MEDICINE.</span></h2>
    <div class="pill">PROGRAMS</div>
    <div class="programs">
      <ul>
        <li><svg width="11" height="11" viewBox="0 0 11 11"><rect x=".5" y=".5" width="10" height="10" fill="none" stroke="#777"/><path d="M2.5 5.5l2 2 4-4.5" fill="none" stroke="#555" stroke-width="1.4"/></svg>Group Fitness and Bootcamp Classes</li>
        <li><svg width="11" height="11" viewBox="0 0 11 11"><rect x=".5" y=".5" width="10" height="10" fill="none" stroke="#777"/><path d="M2.5 5.5l2 2 4-4.5" fill="none" stroke="#555" stroke-width="1.4"/></svg>Individualized Training Classes</li>
        <li><svg width="11" height="11" viewBox="0 0 11 11"><rect x=".5" y=".5" width="10" height="10" fill="none" stroke="#777"/><path d="M2.5 5.5l2 2 4-4.5" fill="none" stroke="#555" stroke-width="1.4"/></svg>Sports Performance Assessment</li>
        <li><svg width="11" height="11" viewBox="0 0 11 11"><rect x=".5" y=".5" width="10" height="10" fill="none" stroke="#777"/><path d="M2.5 5.5l2 2 4-4.5" fill="none" stroke="#555" stroke-width="1.4"/></svg>Metabolic Assessment</li>
      </ul>
      <ul>
        <li><svg width="11" height="11" viewBox="0 0 11 11"><rect x=".5" y=".5" width="10" height="10" fill="none" stroke="#777"/><path d="M2.5 5.5l2 2 4-4.5" fill="none" stroke="#555" stroke-width="1.4"/></svg>Dietary Medicine</li>
        <li><svg width="11" height="11" viewBox="0 0 11 11"><rect x=".5" y=".5" width="10" height="10" fill="none" stroke="#777"/><path d="M2.5 5.5l2 2 4-4.5" fill="none" stroke="#555" stroke-width="1.4"/></svg>Rest and Recovery</li>
        <li><svg width="11" height="11" viewBox="0 0 11 11"><rect x=".5" y=".5" width="10" height="10" fill="none" stroke="#777"/><path d="M2.5 5.5l2 2 4-4.5" fill="none" stroke="#555" stroke-width="1.4"/></svg>Remote Monitoring<br>and Training</li>
      </ul>
    </div>
    <p class="note">*no contracts &nbsp;*month to month</p>
  </div>

  <div class="page inner-right">
    <h2 class="device-title">The Vela Pulseband</h2>
    <p class="device-text">The Vela Pulseband is a modular wearable system with a wristband, arm heart rate monitor and shoe pod that provides clinical grade assessments and captures every activity. The clinical data and assessments we collect with the Vela Pulseband aid in how our physicians, dieticians and fitness specialists create data-driven and personalized wellness programs.</p>
    <div class="brand inner-brand"><span class="brand__dot"></span><span class="brand__name">vela wellness</span></div>
    <div class="shot shot--main" role="img" aria-label="Product visual of clinical quality biometrics measured from the pulse"></div>
    <div class="shot shot--app" role="img" aria-label="Photo of the companion phone app showing biometric data"></div>
    <div class="shot shot--band" role="img" aria-label="Photo of the wearable wristband device"></div>
  </div>

  <div class="pricing">
    <div class="pricing__label">PRICING</div>

    <div class="price-col price-col--fitness">
      <div class="price-box">
        <h3>Group Fitness</h3>
        <ul><li>Unlimited class: $125 per month</li><li>10 pack pass: $100 per month</li><li>Drop in class: $15 per session</li></ul>
      </div>
      <div class="price-box">
        <h3>Peak Performance</h3>
        <p class="rate">$180 PER MONTH</p>
        <ul class="fine"><li>Unlimited Group Classes customized to your biometrics</li><li>Personalized weekly diet plans</li><li>Heart Rate Variability Assessment</li><li>Remote Biometric Monitoring and Training</li></ul>
      </div>
    </div>

    <div class="price-col price-col--testing">
      <div class="price-box">
        <h3>Human Performance Testing</h3>
        <ul><li>VO2 Max Testing: $150</li><li>Resting Metabolic Rate Test: $50</li></ul>
      </div>
      <div class="price-box">
        <h3>Biometric Performance</h3>
        <p class="rate">$555 PER MONTH</p>
        <ul class="fine"><li>Unlimited Group Classes customized to your biometrics</li><li>Personalized weekly diet plans</li><li>Heart Rate Variability Assessment</li><li>Active Heart Rate Monitoring</li><li>Remote Biometric Monitoring and Training</li><li>Sleep Assessment</li><li>Monthly Report</li></ul>
      </div>
    </div>

    <div class="price-col price-col--recovery">
      <div class="price-box">
        <h3>Rest and Recovery Program</h3>
        <ul><li>AirFlow (Power Pants): 1 hour session/ $25, 10 pack one hour sessions/ $200</li><li>Guided Meditation (with EEG assessment) - 1 hour session/ $15</li><li>Guided Meditation and AirFlow - 1 hour session/ $30</li></ul>
      </div>
    </div>
  </div>
</section>

</body>
</html>
```